Brell Harbor Company Business Cards

Front and Back Business Card - logo and text setup - cool design. I need workable photoshop or illustrator files so I can setup each employee card with design that is created
Updates

Hi everyone, thank you for the great entries. Please no more white and blue cards - there are so many already - black and silver only now please. thanks!

Target Market(s)

Construction Industry - Facility Managers

Industry/Entity Type

Construction

Contact Information for Business Card

I really like contemporary simplistic looks - clean neat....not opposed to seeing some black backrounds

Requirements
Must have
• Logo/website address with design on front only - www.brellharbor-example.com (logo attached)
• Back:
• Name/Title/Company Address/Phone/email address
Nice to have
• Cool design
Should not have
• Nothing gimmicky like Fire or Water - since we are a Fire Protection company - it has all been done

```html
<!DOCTYPE html>
<html lang="en">
<head>
<meta charset="utf-8">
<title>Brell Harbor Company – Business Cards</title>
<link href="https://fonts.googleapis.com/css2?family=Roboto+Condensed:wght@400;700&family=Arimo:wght@400&display=swap" rel="stylesheet">
<style>
  :root {
    --page: #e6e6e6;
    --black: #141414;
    --charcoal: #2a2b2d;
    --silver-light: #e4e6e9;
    --silver: #c6c9ce;
    --silver-mid: #a4a8ae;
    --silver-dark: #80858c;
    --steel: #5f646b;
    --rule-dark: #3a3c40;
    --rule-light: #b9bcc1;
  }
  html, body {
    margin: 0;
    width: 1200px;
    height: 1200px;
    overflow: hidden;
    background: var(--page);
  }
  .canvas {
    position: relative;
    width: 1200px;
    height: 1200px;
  }
  .card {
    position: absolute;
    left: 150px;
    width: 900px;
    height: 500px;
    overflow: hidden;
    box-shadow: 0 14px 34px rgba(0,0,0,0.22);
  }
  .card-front {
    top: 70px;
    background: linear-gradient(160deg, #1e1f21 0%, var(--black) 70%);
  }
  .card-back {
    top: 630px;
    background: linear-gradient(160deg, #f4f5f6 0%, var(--silver-light) 100%);
  }

  /* Front */
  .brand {
    position: absolute;
    left: 90px;
    top: 170px;
    display: flex;
    align-items: center;
    gap: 18px;
  }
  .brand-mark {
    width: 24px;
    height: 24px;
    background: var(--silver);
  }
  .brand-name {
    font-family: "Roboto Condensed", sans-serif;
    font-weight: 700;
    font-size: 64px;
    line-height: 1;
    color: var(--silver-light);
  }
  .website {
    position: absolute;
    left: 132px;
    top: 260px;
    margin: 0;
    font-family: "Arimo", sans-serif;
    font-size: 20px;
    letter-spacing: 2px;
    color: var(--silver-mid);
  }

  /* Back */
  .details {
    position: absolute;
    left: 470px;
    top: 70px;
    width: 360px;
  }
  .person-name {
    margin: 0;
    font-family: "Roboto Condensed", sans-serif;
    font-weight: 700;
    font-size: 42px;
    line-height: 1;
    letter-spacing: 1px;
    color: var(--black);
  }
  .person-title {
    margin: 10px 0 0;
    font-family: "Arimo", sans-serif;
    font-size: 16px;
    letter-spacing: 10px;
    color: var(--steel);
  }
  .rule {
    width: 300px;
    height: 1px;
    margin: 20px 0 16px;
    background: var(--rule-light);
  }
  .contact-line {
    margin: 0;
    font-family: "Arimo", sans-serif;
    font-size: 20px;
    line-height: 1.45;
    color: var(--charcoal);
  }
  .back-brand {
    position: absolute;
    left: 70px;
    top: 86px;
    display: flex;
    align-items: center;
    gap: 12px;
  }
  .back-brand .brand-mark { width: 16px; height: 16px; background: var(--black); }
  .back-brand .brand-name { font-size: 34px; color: var(--black); }

  /* Band */
  .band {
    position: absolute;
    left: 0;
    right: 0;
    bottom: 0;
    height: 78px;
    display: flex;
    align-items: flex-end;
    gap: 12px;
  }
  .band-block { height: 100%; }
  .band-block.b1 { flex: 1.3; }
  .band-block.b2 { flex: 1; height: 84%; }
  .band-block.b3 { flex: 1; height: 92%; }
  .band-block.b4 { flex: 0.7; height: 78%; }
  .card-front .b1 { background: var(--silver-light); }
  .card-front .b2 { background: var(--silver); }
  .card-front .b3 { background: var(--silver-mid); }
  .card-front .b4 { background: var(--silver-dark); }
  .card-back .b1 { background: var(--black); }
  .card-back .b2 { background: var(--charcoal); }
  .card-back .b3 { background: var(--steel); }
  .card-back .b4 { background: var(--silver-dark); }
</style>
</head>
<body>
<div class="canvas">
  <section class="card card-front" aria-label="Business card front">
    <div class="brand">
      <span class="brand-mark"></span>
      <span class="brand-name">Brell Harbor</span>
    </div>
    <p class="website">www.brellharbor-example.com</p>
    <div class="band">
      <div class="band-block b1"></div>
      <div class="band-block b2"></div>
      <div class="band-block b3"></div>
      <div class="band-block b4"></div>
    </div>
  </section>

  <section class="card card-back" aria-label="Business card back">
    <div class="back-brand">
      <span class="brand-mark"></span>
      <span class="brand-name">Brell Harbor</span>
    </div>
    <div class="details">
      <h1 class="person-name">MAREN COLT</h1>
      <p class="person-title">FOUNDER</p>
      <div class="rule"></div>
      <p class="contact-line">555-014-2290</p>
      <p class="contact-line">info@brellharbor.example</p>
      <div class="rule"></div>
      <p class="contact-line">48 Quarry Lane</p>
      <p class="contact-line">Port Alden, NY 10990</p>
    </div>
    <div class="band">
      <div class="band-block b1"></div>
      <div class="band-block b2"></div>
      <div class="band-block b3"></div>
      <div class="band-block b4"></div>
    </div>
  </section>
</div>
</body>
</html>
```